「アオバリンク」をぜひ利用してみたいと思わせる構成をお願いいたします。企業採用活動に関して信頼を置いて相談ができることを意識させるイメージでデザインを希望いたします。
イメージキーワード : 爽やか、現代的、おしゃれ

構成、文章に関しましては添付のラフ案をご参照ください。
一枚物のLPでフォームが表示されるイメージです。

※スマホ版・PC版双方のデザインをお願いいたします。

参考デザインとしてURLを記載いたします。
レイアウトベースイメージはこちら「ひらけの仕事」
https://hirake-shigoto.com/html/pr/ad/pc/basic/3040/009/

デザインイメージはこちら「東陽コルディア」
https://www.kordia-toyo.jp/recruit/

※ひらけの仕事のレイアウトをベースに色味、写真・イラストの雰囲気は「東陽コルディア」のイメージです。

納品データはaiデータでお願いいたします。
1枚もののページでPC版の幅は1000px、スマホ版の幅は750pxで製作予定です。

素材に関しましてはゆるえ素材庫・フォトノハラのアカウントを保有しておりますのでそちらのカンプデータをなるべくご使用いただけましたら幸いです。
※イメージに合う物がない場合、別素材でもかまいません。
https://k-sparrow.com/

素晴らしいデザインで、当方のイメージ合わせご制作いただきありがとうございました。

皆様、この度は弊社のLPのデザインコンペに多数ご応募いただきましてありがとうございました。
また、コンペでの発注をさせていただくことがありました際は、何卒よろしくお願い申し上げます。

```html
<!DOCTYPE html>
<html lang="ja">
<head>
<meta charset="utf-8">
<title>アオバリンク｜管理者採用支援サービス</title>
<link href="https://fonts.googleapis.com/css2?family=Noto+Sans+JP:wght@400;500;700&family=Cormorant+Garamond:ital,wght@1,400&display=swap" rel="stylesheet">
<style>
:root{
  --hero-bg:#8ea3b2;
  --hero-deep:#6f8799;
  --ink:#333b42;
  --muted:#59636b;
  --accent:#4e7ea6;
  --accent-dark:#3d6a90;
  --box-head:#5f95bb;
  --tag:#4f81aa;
  --pale:#f3f6f8;
  --line:#c9d2d9;
  --case-bg:#5d7187;
  --case-deep:#4b5e73;
  --white:#ffffff;
}
*{box-sizing:border-box;margin:0;padding:0}
html,body{width:1200px;height:4420px;overflow:hidden}
body{font-family:"Noto Sans JP",sans-serif;color:var(--ink);background:var(--white);position:relative}
section{position:absolute;left:0;width:1200px}
.btn{position:absolute;left:50%;transform:translateX(-50%);background:var(--accent);color:var(--white);font-size:17px;font-weight:500;letter-spacing:.05em;width:400px;height:60px;display:flex;align-items:center;justify-content:center;box-shadow:0 3px 0 var(--accent-dark)}
.script{position:absolute;font-family:"Cormorant Garamond",serif;font-style:italic;color:rgba(120,150,175,.18);font-size:140px;line-height:1}

/* hero */
.hero{top:0;height:740px;background:linear-gradient(135deg,var(--hero-bg),var(--hero-deep))}
.hero-photo{position:absolute;inset:0;background:linear-gradient(160deg,rgba(180,196,208,.35),rgba(90,112,130,.25))}
.hero-art{position:absolute;left:400px;top:20px;width:230px;height:200px;background:linear-gradient(180deg,rgba(255,255,255,.18),rgba(255,255,255,.04))}
.hero-lead{position:absolute;left:120px;top:120px;color:var(--white);font-size:40px;font-weight:500;letter-spacing:.08em}
.hero-sub{position:absolute;left:120px;top:270px;color:var(--white);font-size:38px;font-weight:500;line-height:1.6;letter-spacing:.04em}
.hero-brand{position:absolute;left:120px;top:405px;color:var(--white);font-size:48px;font-weight:700;letter-spacing:.08em}
.hero-tags{position:absolute;left:30px;top:560px;display:flex;gap:18px}
.hero-tags span{background:var(--tag);color:var(--white);font-size:24px;font-weight:500;padding:12px 20px}
.form{position:absolute;left:810px;top:20px;width:350px;height:530px;background:var(--white);padding:28px 26px}
.field{height:58px;border:1px solid var(--line);margin-bottom:18px;padding:0 16px;display:flex;align-items:center;font-size:15px;color:#9aa3aa}
.form-btn{margin-top:14px;height:58px;background:var(--accent);color:var(--white);font-size:15px;font-weight:500;display:flex;align-items:center;justify-content:center}
.form-note{margin-top:18px;font-size:13px;line-height:1.7;color:var(--ink)}

/* worries */
.worries{top:740px;height:1180px;background:var(--white)}
.worries-art{position:absolute;left:60px;top:50px;width:190px;height:200px;background:linear-gradient(180deg,#c9d8e3,#e9eff3)}
.worries .script{right:120px;top:195px}
.sec-title{position:absolute;left:0;width:1200px;text-align:center;font-size:34px;font-weight:500;line-height:1.45;color:var(--ink)}
.worry-list{position:absolute;left:100px;top:290px;width:1000px;display:flex;justify-content:space-between}
.worry{width:300px;height:290px;border:3px solid var(--box-head);background:var(--white)}
.worry h3{background:var(--box-head);color:var(--white);text-align:center;font-size:21px;font-weight:500;padding:12px 0}
.worry-pic{width:200px;height:140px;margin:22px auto 14px;background:linear-gradient(135deg,#b9ccda,#e1e9ef)}
.worry p{text-align:center;font-size:17px;font-weight:500}
.worries-body{position:absolute;left:190px;top:640px;width:820px;font-size:17px;line-height:2.1;color:var(--ink)}
.worries .btn{top:1075px}

/* reasons */
.reasons{top:1920px;height:940px;background:linear-gradient(180deg,#eef2f5,#f7f9fa)}
.reasons .script{right:110px;top:30px}
.reason-list{position:absolute;left:70px;top:245px;width:1060px;display:flex;justify-content:space-between}
.reason{width:330px;height:390px;background:var(--white);padding:30px 28px;text-align:center}
.reason h3{font-size:23px;font-weight:700;line-height:1.4;height:64px;display:flex;align-items:center;justify-content:center}
.reason-icon{width:110px;height:110px;margin:22px auto 26px;border-radius:6px}
.reason p{font-size:16px;line-height:1.9;text-align:left}
.reasons .btn{top:780px}

/* cases */
.cases{top:2860px;height:1560px;background:linear-gradient(180deg,var(--case-bg),var(--case-deep))}
.cases-photo{position:absolute;inset:0;background:linear-gradient(120deg,rgba(160,180,200,.18),rgba(60,75,90,.1))}
.cases .script{left:560px;top:0;color:rgba(255,255,255,.15)}
.cases .sec-title{color:var(--white);top:140px}
.case{position:absolute;left:160px;width:880px;background:var(--white);border-collapse:collapse;font-size:15px}
.case th,.case td{border:1px solid var(--line);padding:7px 14px;vertical-align:middle;text-align:left}
.case th{width:150px;font-weight:500;text-align-last:justify;text-align:justify;background:#f5f7f9}
.case td.story{line-height:1.75;font-size:14px}
.cases-note{position:absolute;left:180px;top:1390px;color:var(--white);font-size:15px}
.cases .btn{top:1455px}
</style>
</head>
<body>

<section class="hero">
  <div class="hero-photo" role="img" aria-label="ビジネスパーソンと街並みの写真"></div>
  <div class="hero-art" role="img" aria-label="階段を上るビジネスパーソンのイラスト"></div>
  <p class="hero-lead">会社の将来を託せる</p>
  <h1 class="hero-sub">30代〜40代ミドル層<br>管理者採用支援サービス</h1>
  <p class="hero-brand">アオバリンク</p>
  <div class="hero-tags"><span>管理職・幹部候補</span><span>年収 600 万円</span><span>優良人材</span></div>
  <div class="form">
    <div class="field">会社名</div>
    <div class="field">担当者名</div>
    <div class="field">メールアドレス</div>
    <div class="form-btn">登録して資料をダウンロードする</div>
    <p class="form-note">この資料は、なぜ管理職が不足しているのか？管理職を社外登用することのメリットなど今後の対策方法をまとめた「ミドル層管理者のための人材採用レポート」がダウンロードできます。</p>
  </div>
</section>

<section class="worries">
  <div class="worries-art" role="img" aria-label="考え込むビジネスパーソンのイラスト"></div>
  <div class="script">Worries</div>
  <h2 class="sec-title" style="top:190px">【こんな課題ありませんか？】<br>管理職採用における３つの悩み</h2>
  <div class="worry-list">
    <div class="worry"><h3>【新規事業への挑戦】</h3><div class="worry-pic" role="img" aria-label="人材が見つからない様子のイラスト"></div><p>社内に適任者がいない！</p></div>
    <div class="worry"><h3>【DX 強化】</h3><div class="worry-pic" role="img" aria-label="デジタル化に戸惑う様子のイラスト"></div><p>いきなりいわれても困る！</p></div>
    <div class="worry"><h3>【社内公募・推薦】</h3><div class="worry-pic" role="img" aria-label="候補者を探す様子のイラスト"></div><p>管理職候補者がいない！</p></div>
  </div>
  <p class="worries-body">近年の国の施策に沿った働き方改革や新規事業への挑戦、ＳＤＧｓ（持続可能な開発目標）、ＤＸ（デジタルトランスフォーメーション）、ＧＸ（グリーントランスフォーメーション）、カーボンニュートラル等への対策のため多くの企業が取り組みを始めています。<br>しかし多くの中小企業はそれらの取り組みのための中心的人材が不足しており対応できる人材確保が経営課題の一つになっていますが社内に適任者はなかなかおらず外部から調達をしなければなりません。<br>その人材採用における問題解決を当社にお任せください。<br>貴社専任の採用専門コンサルタントが貴社に必要な人材をあぶり出し採用を成功に導きます！<br>詳しくは、当社がまとめた「ミドル層管理者のための人材採用レポート」をご覧ください。</p>
  <div class="btn">登録して資料をダウンロードする</div>
</section>

<section class="reasons">
  <div class="script">Reasons</div>
  <h2 class="sec-title" style="top:170px">管理職採用でアオバリンクが選ばれる３つの理由</h2>
  <div class="reason-list">
    <div class="reason"><h3>手間が省ける</h3><div class="reason-icon" role="img" aria-label="書類のアイコン" style="background:linear-gradient(135deg,#4f8fb0,#7db6c9)"></div><p>求人作成、応募者対応等面倒な業務が軽減できます！</p></div>
    <div class="reason"><h3>エンゲージメント<br>低下抑制</h3><div class="reason-icon" role="img" aria-label="鍵のアイコン" style="background:linear-gradient(135deg,#9a5fa8,#c98cc4)"></div><p>大々的に管理職を募集しないため社内外に漏れずに採用ができる！</p></div>
    <div class="reason"><h3>ピンポイント採用<br>が可能</h3><div class="reason-icon" role="img" aria-label="人物選定のアイコン" style="background:linear-gradient(135deg,#e0a23d,#f0c76e)"></div><p>●●社の経験者、●●プロジェクトの経験者など、希望に応じてサーチすることが可能です！</p></div>
  </div>
  <div class="btn">登録して資料をダウンロードする</div>
</section>

<section class="cases">
  <div class="cases-photo" role="img" aria-label="オフィスで打ち合わせする人々の写真"></div>
  <div class="script">Case study</div>
  <h2 class="sec-title">当社アオバリンク成功事例</h2>

  <table class="case" style="top:200px">
    <tr><th>社名</th><td>A社</td></tr>
    <tr><th>業種</th><td>アウトソーシング企業</td></tr>
    <tr><th>社員数</th><td>4200 名（グループ全体）</td></tr>
    <tr><th>募集職種</th><td>【新部署立ち上げ】デジタルマーケティング責任者</td></tr>
    <tr><th>採用成功<br>ストーリー</th><td class="story">今後の事業展開の一環として社内外にある情報を IT 技術で収集して分析、戦略を練ることが必要な部門を立ち上げるためにご依頼。社内に適任者がおらず当社にご相談いただき、当社ダイレクトリクルーティングにてマーケティング経験の豊富な人材をご紹介。現在はデジタル戦略部の責任者として部署を牽引されています。</td></tr>
  </table>

  <table class="case" style="top:620px">
    <tr><th>社名</th><td>S社</td></tr>
    <tr><th>業種</th><td>通販業</td></tr>
    <tr><th>社員数</th><td>700 名</td></tr>
    <tr><th>募集職種</th><td>営業企画ディレクター</td></tr>
    <tr><th>採用成功<br>ストーリー</th><td class="story">自社内の営業企画部門の強化のために部門長クラスの人材採用を計画。当社にご依頼いただき、当社独自のネットワークを駆使し同業界出身で 20 年以上のキャリアを持つ人材を採用に成功。</td></tr>
  </table>

  <table class="case" style="top:1005px">
    <tr><th>社名</th><td>O社</td></tr>
    <tr><th>業種</th><td>旅館ホテル業</td></tr>
    <tr><th>社員数</th><td>150 名</td></tr>
    <tr><th>募集職種</th><td>【新規立ち上げ】ホテルのサービス責任者</td></tr>
    <tr><th>採用成功<br>ストーリー</th><td class="story">リゾート地に特化したホテルを運営している同社にて海外ブランドとのライセンス契約による新規ホテル開業を控え責任者の採用をご依頼。当社のダイレクトリクルーティングを駆使し、国内の高級ホテルでの勤務経験があり語学にも長けた人材の採用に成功。</td></tr>
  </table>

  <p class="cases-note">これは、一例です。その他人材採用支援実績があります。</p>
  <div class="btn">登録して資料をダウンロードする</div>
</section>

</body>
</html>
```